Web design for a dental and eye clinic

We need a web design for a dental and eye clinic ( with medical laboratory services) with two branches in Lagos Nigeria. The ultimate aim is to attract more patronage. The design should have links to social media and should have provision for appointments and enquiries. Blue should be part of the colours

Name of facility. VORANTECLINICS Added Saturday, May 27, 2017

Target Market(s)

Lagos. Nigeria

Industry/Entity Type

Health Care

Number of Pages Required

3 page

Font styles to use
Sans Serif

Colors
85cae6
cadf82

Requirements
Must have
• a projection of the professioal services rendered
Nice to have
• portal for enquiries and appointments
• Link to our facebook, twitter and instagram

```html
<!DOCTYPE html>
<html lang="en">
<head>
<meta charset="utf-8">
<title>Vorante Clinics – Eye and Dental Care</title>
<link href="https://fonts.googleapis.com/css2?family=Lato:wght@400;700;900&family=Open+Sans:wght@400;600;700&display=swap" rel="stylesheet">
<style>
:root{
  --navy:#23318a;
  --blue:#1ea6e3;
  --sky:#85cae6;
  --lime:#cadf82;
  --red:#d8342b;
  --ink:#2b2b2b;
  --grey:#777;
  --line:#e3e3e3;
  --pale:#d6eaf4;
  --dark:#1f1f1f;
}
*{box-sizing:border-box;margin:0;padding:0}
html,body{width:1200px;height:3448px;overflow:hidden}
body{font-family:"Open Sans",Arial,sans-serif;color:var(--ink);background:#fff;position:relative}
.abs{position:absolute}
.topbar{left:0;top:0;width:1200px;height:32px;background:#f1f1f1;border-bottom:1px solid var(--line);font-size:11px;color:#888}
.topbar .social{left:80px;top:9px;display:flex;gap:18px}
.dot{width:13px;height:13px;border-radius:50%;background:#9a9a9a;display:block}
.topbar .links{right:80px;top:8px;display:flex;gap:28px;text-transform:uppercase;font-weight:600}
.header{left:0;top:32px;width:1200px;height:120px}
.brand{left:80px;top:20px;display:flex;align-items:center;gap:12px}
.brand .mark{width:56px;height:56px;border-radius:50%;background:var(--blue)}
.brand .name{font-family:"Lato",sans-serif;font-weight:900;font-size:30px;color:var(--navy);line-height:1}
.info{display:flex;gap:12px;align-items:flex-start;font-size:13px;color:#555;line-height:18px;white-space:nowrap}
.info svg{flex:none;margin-top:2px}
.info b{color:var(--ink);font-weight:700}
.nav{left:80px;top:152px;width:1040px;height:46px;background:var(--navy);display:flex;align-items:center}
.nav a{color:#fff;text-decoration:none;font-size:11px;font-weight:700;text-transform:uppercase;padding:0 12px;height:46px;line-height:46px;white-space:nowrap}
.nav a.active{background:var(--blue)}
.nav .search{margin-left:auto;width:46px;height:46px;background:var(--blue);display:flex;align-items:center;justify-content:center}
.hero{left:0;top:200px;width:1200px;height:580px;background:linear-gradient(90deg,#f3f3f3 0%,#e9ecef 35%,#c9d3c2 60%,#b8c7a8 100%)}
.hero-photo{left:360px;top:0;width:840px;height:580px;background:radial-gradient(ellipse at 55% 55%,#e6c9b3 0%,#cfb6a0 30%,#aebc98 65%,#97ad86 100%)}
.hero-title{left:80px;top:370px;font-family:"Lato",sans-serif;font-weight:900;font-size:52px;color:#222;line-height:60px;white-space:nowrap}
.hero-text{left:80px;top:440px;width:340px;font-size:15px;color:#555;line-height:22px}
.btn{display:inline-block;color:#fff;font-size:14px;font-weight:700;text-align:center}
.hero-btn{top:528px;width:140px;height:42px;line-height:42px}
.card{width:320px;top:852px}
.card .photo{width:320px;height:170px}
.card h3{font-family:"Lato",sans-serif;font-weight:900;font-size:24px;margin:30px 0 10px;color:#222}
.card p{font-size:13px;color:#888;line-height:20px;height:120px}
.card .btn{width:320px;height:44px;line-height:44px;font-size:15px}
.quick{left:800px;top:852px;width:328px;border:1px solid var(--line);background:#fff}
.quick li{list-style:none;display:flex;align-items:center;gap:16px;height:58px;padding:0 20px;border-bottom:1px solid var(--line);font-size:11px;font-weight:700;color:#555;text-transform:uppercase}
.quick li:last-child{border-bottom:none}
.quick i{width:22px;height:22px;border-radius:4px;background:#b9b9b9;display:block}
.finder{left:0;top:1348px;width:1200px;height:452px;background:linear-gradient(180deg,#5b6670 0%,#48525c 50%,#3d4650 100%)}
.finder h2{position:absolute;left:0;top:44px;width:1200px;text-align:center;font-family:"Lato",sans-serif;font-weight:900;font-size:38px;line-height:46px;color:#fff}
.row{position:absolute;left:140px;display:flex;align-items:center;width:720px}
.row label{width:200px;text-align:right;padding-right:14px;color:#fff;font-size:14px;white-space:nowrap}
.row .field{width:520px;height:36px;background:#fff;font-size:12px;color:#999;padding:0 12px;line-height:36px;display:flex;justify-content:space-between}
.or{position:absolute;left:340px;top:1582px;width:520px;text-align:center;color:#fff;font-size:16px;font-weight:700}
.or:before,.or:after{content:"";position:absolute;top:11px;width:220px;height:1px;background:rgba(255,255,255,.5)}
.or:before{left:0}.or:after{right:0}
.submit{left:340px;top:1690px;width:520px;height:52px;line-height:52px;background:var(--red);font-size:20px}
.video{left:168px;top:1872px;width:840px;height:480px;background:linear-gradient(110deg,#3b3f43 0%,#a8a39a 40%,#6d6f70 70%,#2c2f33 100%)}
.video .play{left:380px;top:200px;width:80px;height:80px;border-radius:50%;background:rgba(255,255,255,.85)}
.video .bar{left:0;bottom:0;width:840px;height:40px;background:rgba(0,0,0,.7)}
.video .track{left:80px;top:18px;width:620px;height:4px;background:#777}
.video .track span{display:block;width:60px;height:4px;background:var(--blue)}
.stories{left:0;top:2420px;width:1200px;height:388px;background:var(--pale)}
.stories h2{position:absolute;left:100px;top:60px;font-family:"Lato",sans-serif;font-weight:900;font-size:36px;color:var(--navy)}
.stories .quote{position:absolute;left:100px;top:118px;font-size:20px;color:#333}
.stories .avatar{position:absolute;left:100px;top:180px;width:110px;height:200px;background:linear-gradient(180deg,#cfe0ec,#7fa8c8)}
.stories .text{position:absolute;left:240px;top:210px;width:400px;font-size:13px;color:#555;line-height:20px}
.stories .brand2{position:absolute;left:760px;top:160px;display:flex;align-items:center;gap:16px}
.brand2 .mark{width:90px;height:90px;border-radius:50%;background:var(--blue)}
.brand2 .name{font-family:"Lato",sans-serif;font-weight:900;font-size:32px;color:var(--navy);white-space:nowrap}
.register{left:0;top:2808px;width:1200px;height:304px;text-align:center}
.register h2{margin-top:92px;font-family:"Lato",sans-serif;font-weight:900;font-size:28px;letter-spacing:1px}
.register p{width:560px;margin:18px auto 0;font-size:14px;color:#777;line-height:22px}
.register .btns{margin-top:26px;display:flex;justify-content:center;gap:40px}
.register .btns span{width:180px;height:40px;line-height:40px;font-size:11px;font-weight:700}
.footer{left:0;top:3112px;width:1200px;height:336px;background:var(--dark);text-align:center;color:#bbb}
.footer .brand3{margin:56px auto 0;display:flex;justify-content:center;align-items:center;gap:14px}
.brand3 .mark{width:60px;height:60px;border-radius:50%;background:#fff}
.brand3 .name{font-family:"Lato",sans-serif;font-weight:900;font-size:32px;color:#fff}
.footer nav{margin-top:56px;display:flex;justify-content:center;gap:34px;font-size:12px;font-weight:700;color:#fff}
.footer small{display:block;margin-top:14px;font-size:12px;color:#999}
.footer .soc{margin-top:30px;display:flex;justify-content:center;gap:14px}
.footer .soc i{width:28px;height:28px;border-radius:50%;background:#3a3a3a;display:block}
</style>
</head>
<body>

<div class="abs topbar">
  <div class="abs social"><i class="dot"></i><i class="dot"></i><i class="dot"></i></div>
  <div class="abs links"><span>Book your visit</span><span>Programme Nominations</span><span>Relationship Counselling</span></div>
</div>

<header class="abs header">
  <div class="abs brand"><span class="mark"></span><span class="name">VORANTECLINICS</span></div>
  <div class="abs info" style="left:488px;top:40px">
    <svg width="20" height="20" viewBox="0 0 24 24"><path d="M6.6 10.8a15 15 0 0 0 6.6 6.6l2.2-2.2c.3-.3.7-.4 1-.2 1.1.4 2.3.6 3.6.6.6 0 1 .4 1 1V20c0 .6-.4 1-1 1C10.6 21 3 13.4 3 4c0-.6.4-1 1-1h3.5c.6 0 1 .4 1 1 0 1.3.2 2.5.6 3.6.1.3 0 .7-.2 1z" fill="#555"/></svg>
    <div><b>1 200 555 0147</b><br>hello@voranteclinics.example</div>
  </div>
  <div class="abs info" style="left:736px;top:40px">
    <svg width="18" height="22" viewBox="0 0 24 24"><path d="M12 2a7 7 0 0 0-7 7c0 5 7 13 7 13s7-8 7-13a7 7 0 0 0-7-7zm0 9.5A2.5 2.5 0 1 1 12 6.5a2.5 2.5 0 0 1 0 5z" fill="#555"/></svg>
    <div><b>48 Marina Crescent,</b><br>Suite 12, Victoria Island, Lagos</div>
  </div>
  <div class="abs info" style="left:984px;top:40px">
    <svg width="20" height="20" viewBox="0 0 24 24"><circle cx="12" cy="12" r="9" fill="none" stroke="#555" stroke-width="2"/><path d="M12 7v5l3 2" stroke="#555" stroke-width="2" fill="none"/></svg>
    <div><b>7:00 AM – 7:00 PM</b><br>Monday to Saturday</div>
  </div>
</header>

<nav class="abs nav">
  <a class="active">Home</a><a>About</a><a>Resources</a><a>Counselling FAQ</a><a>Relationship Counselling</a><a>Our Therapy Locations</a><a>Success</a><a>F.A.Q's</a><a>Blog</a><a>Shop Cart</a>
  <span class="search"><svg width="18" height="18" viewBox="0 0 24 24"><circle cx="10" cy="10" r="6" stroke="#fff" stroke-width="2.5" fill="none"/><path d="M15 15l5 5" stroke="#fff" stroke-width="2.5"/></svg></span>
</nav>

<section class="abs hero">
  <div class="abs hero-photo" role="img" aria-label="Smiling family of four posing together outdoors"></div>
</section>
<h1 class="abs hero-title">Eye and Dental care</h1>
<p class="abs hero-text">Is a company passionate about creating healthy, happy smiles and clear vision, for all ages.</p>
<span class="abs btn hero-btn" style="left:80px;background:var(--navy)">Read More</span>
<span class="abs btn hero-btn" style="left:236px;background:var(--blue)">Contact Us</span>

<article class="abs card" style="left:80px">
  <div class="photo" role="img" aria-label="Dentist treating a patient in the dental chair" style="background:linear-gradient(135deg,#7fc3e6,#d9e9f2 60%,#b7cfde)"></div>
  <h3>Vorante Dental Care</h3>
  <p>Our dental team offers gentle checkups, cleaning, fillings, whitening and orthodontic care for the whole family, using modern equipment in a calm and friendly setting at both branches.</p>
  <span class="btn" style="background:var(--blue)">Read More</span>
</article>

<article class="abs card" style="left:440px">
  <div class="photo" role="img" aria-label="Woman having an eye examination with a phoropter" style="background:linear-gradient(135deg,#d8d2cb,#a9a39c 50%,#ede8e2)"></div>
  <h3>Vorante Eye Care</h3>
  <p>Our eye care team provides full vision tests, glasses and lens fitting, eye disease screening and laboratory services, helping patients of every age see clearly and keep their eyes healthy.</p>
  <span class="btn" style="background:#cfcfcf;color:#555">Read More</span>
</article>

<ul class="abs quick">
  <li><i></i>Patient Forms</li>
  <li><i></i>Insurance Plan Participants</li>
  <li><i></i>Make a Payment</li>
  <li><i></i>Order Contact Lenses</li>
  <li><i></i>Request Appointment</li>
  <li><i></i>Before &amp; After</li>
</ul>

<section class="abs finder" role="img" aria-label="Blurred clinic interior in grey-blue tones">
  <h2>Find Our Dentis and Eye care Near You</h2>
  <div class="row" style="top:124px"><label>Type of Counselling:</label><span class="field">Select <svg width="10" height="10" viewBox="0 0 10 10" style="margin-top:13px"><path d="M1 3l4 4 4-4" stroke="#666" fill="none" stroke-width="1.5"/></svg></span></div>
  <div class="row" style="top:180px"><label>Location:</label><span class="field"></span></div>
  <div class="row" style="top:280px"><label>Postcode:</label><span class="field"></span></div>
</section>
<div class="or">OR</div>
<span class="abs btn submit">Submit</span>

<div class="abs video" role="img" aria-label="Video still of an optometrist examining an elderly man's eyes">
  <span class="abs play"></span>
  <svg class="abs" style="left:410px;top:222px" width="28" height="36" viewBox="0 0 28 36"><path d="M0 0l28 18L0 36z" fill="#333"/></svg>
  <div class="abs bar"><div class="abs track"><span></span></div></div>
</div>

<section class="abs stories">
  <h2>SUCCESS STORIES</h2>
  <div class="quote">At the end of our life, what matters most is how well did we love”</div>
  <div class="avatar" role="img" aria-label="Portrait of a smiling clinician in scrubs"></div>
  <div class="text">You can read more about relationship counselling here.<br>Warmly,<br>Ruth, Dana Morrow<br>Director – Psychologist<br>Grad Dip Psych, Post Grad Dip Psych, B.Sc Dip Teach, MAPS</div>
  <div class="brand2"><span class="mark"></span><span class="name">VORANTECLINICS</span></div>
</section>

<section class="abs register">
  <h2>REGISTER TO RECEIVE UPDATES</h2>
  <p>We are continuously making improvements and innovations in products that can help you. Stay current with our updates.</p>
  <div class="btns"><span class="btn" style="background:var(--blue)">SUBSCRIBE</span><span class="btn" style="background:#fff;color:#666;border:1px solid #ccc">LOG IN</span></div>
</section>

<footer class="abs footer">
  <div class="brand3"><span class="mark"></span><span class="name">VORANTECLINICS</span></div>
  <nav><span>HOME</span><span>ABOUT</span><span>RESOURCES</span><span>BLOG</span><span>SHOP CART</span></nav>
  <small>Copyright © 2016 Vorante Clinics. All rights reserved.</small>
  <div class="soc"><i></i><i></i><i></i></div>
</footer>

</body>
</html>
```